Legal and business training card design

We need a business card design for POBAK - Pastoral Owners Bureau and Knowhow Agency a new company set up in county Victoria . Our aim is to assist regional business with their every day employment law legal issues and questions - this would include compliance within the workplace, employment conts, EBAs, dismissals, and general OHS. As well as POBAK will engage in training in particular Human Resources, management v leadership, time management , as well as constructing training around individual business/s needs. So we are multi purpose.
Our product is our service. It's designed specifically for regional base business hence we understand the requirements and needs of regional business v city business. At the same time the card must be simple, yet hard hitting, getting the message across in a couple of seconds.
I would like to see red and yellows, with perhaps a symbol/logo that represents the regional areas incorporated into the POBAK name ie curvy R in which the R's " right leg "expands under the entire acronym. Or you may have some better ideas. I also like the symbol of the square/s to match our slogan "Practical Workplace Solutions Beyond The Boundary Fence".
Thanks
Industry/Entity Type
Training
Contact Information for Business Card
POBAK
Pastoral Owners Bureau & Knowhow Agency
"Practical Workplace Solutions Beyond The Boundary Fence"
Fiona Brack B.A LL.B
Director and Principal
T: 1800 927 418 E: fiona@pobak.com.au
W: www.pobak.com.au

```html
<!DOCTYPE html>
<html lang="en">
<head>
<meta charset="utf-8">
<title>POBAK Business Card</title>
<link rel="stylesheet" href="https://fonts.googleapis.com/css2?family=Lato:wght@400;700&display=swap">
<style>
  :root {
    --backdrop: #555555;
    --card: #1e1e1e;
    --red: #e0262b;
    --yellow: #f2d21b;
    --amber: #f5a31a;
  }
  * { margin: 0; padding: 0; box-sizing: border-box; }
  html, body {
    width: 1200px;
    height: 1000px;
    overflow: hidden;
  }
  body {
    background: var(--backdrop);
    font-family: "Lato", Arial, sans-serif;
    position: relative;
  }
  .card {
    position: absolute;
    top: 185px;
    width: 389px;
    height: 630px;
    background: var(--card);
    text-align: center;
    overflow: hidden;
  }
  .card--front { left: 181px; }
  .card--back { left: 605px; }

  .brand {
    position: absolute;
    top: 96px;
    left: 0;
    right: 0;
    height: 76px;
    display: flex;
    justify-content: center;
    align-items: center;
    gap: 14px;
  }
  .brand__square {
    width: 30px;
    height: 30px;
    background: var(--yellow);
  }
  .brand__name {
    color: var(--red);
    font-weight: 700;
    font-size: 58px;
    letter-spacing: 10px;
    line-height: 1;
  }
  .company {
    position: absolute;
    top: 183px;
    left: 0;
    right: 0;
    color: var(--red);
    font-weight: 700;
    font-size: 22px;
    line-height: 27px;
  }
  .tagline {
    position: absolute;
    top: 479px;
    left: 0;
    right: 0;
    color: var(--red);
    font-weight: 700;
    font-size: 19px;
    line-height: 28px;
  }
  .person {
    position: absolute;
    top: 331px;
    left: 0;
    right: 0;
  }
  .person__name {
    color: var(--amber);
    font-weight: 700;
    font-size: 26px;
    line-height: 30px;
  }
  .person__detail {
    color: var(--red);
    font-size: 18px;
    line-height: 26px;
  }
  .contact {
    position: absolute;
    top: 451px;
    left: 0;
    right: 0;
    list-style: none;
    font-size: 18px;
    line-height: 28.5px;
    color: var(--red);
  }
  .contact__label {
    font-weight: 700;
    color: var(--yellow);
  }
  .contact__label--phone { color: var(--amber); }
  .pattern-band {
    position: absolute;
    left: 0;
    right: 0;
    bottom: 0;
    height: 42px;
    background: linear-gradient(to bottom, var(--red) 0%, var(--red) 8%, var(--yellow) 30%, var(--yellow) 70%, var(--red) 92%, var(--red) 100%);
  }
</style>
</head>
<body>
  <section class="card card--front">
    <div class="brand">
      <span class="brand__name">POBAK</span>
      <span class="brand__square"></span>
    </div>
    <p class="company">Pastoral Owners Bureau<br>&amp; Knowhow Agency</p>
    <p class="tagline">Practical Workplace Solutions<br>Beyond The Boundary Fence</p>
    <div class="pattern-band" role="img" aria-label="Decorative red band with a row of yellow squares"></div>
  </section>

  <section class="card card--back">
    <div class="brand">
      <span class="brand__name">POBAK</span>
      <span class="brand__square"></span>
    </div>
    <p class="company">Pastoral Owners Bureau<br>&amp; Knowhow Agency</p>
    <div class="person">
      <p class="person__name">Fiona Brack</p>
      <p class="person__detail">B.A., LL.B.</p>
      <p class="person__detail">Director and Principal</p>
    </div>
    <ul class="contact">
      <li><span class="contact__label contact__label--phone">T:</span> 1800 927 418</li>
      <li><span class="contact__label">E:</span> fiona@pobak.com.au</li>
      <li><span class="contact__label">W:</span> www.pobak.com.au</li>
    </ul>
    <div class="pattern-band" role="img" aria-label="Decorative red band with a row of yellow squares"></div>
  </section>
</body>
</html>
```